Three Banner Ad Concepts Multiple Sizes For Murmuro Native Ads Network Campaigns

I would like to see THREE totally different concepts using the content below. Once I approve the THREE DESIGN CONCEPTS I will need them in 5 different sizes for each of the 3 approved concepts.

So technically I am asking for THREE totally different designs in FIVE Sizes. See Sizes below.

I will advertise these banners on vorpla ad display network, tenvixads.example as well as murmuro so please keep these in mind and if you have experience creating these type of ads then this is great.

Headlines:
1. Boost Responses To Your Ads Without Increasing Ad Spend Giving Away Free Smartwatches and Sonettes You Don't Personally Need To Fulfill!

2. Attract More Customers During Tough Times Giving Away Free Vacation & Dining Vouchers That You Don't Need To Pay For!

3. Increase Conversions On Your Website Offering A Free Hotel Stay Or Even A Smart Watch In Exchange For Their Form Submission!

Calls To Actions:
1. Get A Free Sample Package
2. Sign Up For A Free Trial
3. Book A Demo

Native Ads Sizes
Image Size 600x600
Image Size 600x500
Image Size 600x315

Murmuro (for mm ads please take into account the 20% text rule in the image):
For carousel: 1200x1200 pixels
For regular image ads: 1200x628 pixels

Target Market(s)

B2B, Small Business Owners, Entrepreneurs, Marketing Directors, Sales Managers

Industry/Entity Type

Marketing

Requirements
Must have
• Use images from quarrypix.example as I have account here
Nice to have
• These designs need to be B2B based....Use images that compliment the TEXT and speak to a BUSINESS OWNER and NOT A CONSUMER!!
Should not have
• DO NOT CREATE AN AD THAT IS B2C based, this is a B2B ad. please check website www.bluefernrewardgroup.example

```html
<!DOCTYPE html>
<html lang="en">
<head>
<meta charset="utf-8">
<title>Bluefern Reward Group – Free Smartwatches and Sonettes</title>
<link rel="stylesheet" href="https://fonts.googleapis.com/css2?family=Montserrat:ital,wght@0,400;0,600;0,700;0,800;1,700;1,800&display=swap">
<style>
  :root {
    --brand-blue: #1b72bf;
    --accent-orange: #f7941d;
    --ink: #1d1d1d;
    --paper: #ffffff;
    --mist: #dde3ea;
    --photo-light: #d9cbbd;
    --photo-mid: #b9a08c;
    --photo-dark: #5d6470;
  }
  html, body {
    margin: 0;
    padding: 0;
    overflow: hidden;
    background: var(--paper);
  }
  .ad-canvas {
    position: relative;
    width: 1200px;
    height: 1200px;
    overflow: hidden;
    font-family: "Montserrat", sans-serif;
    background: var(--paper);
  }
  .hero-photo {
    position: absolute;
    inset: 0;
    background:
      radial-gradient(ellipse at 55% 45%, var(--photo-light) 0%, var(--photo-mid) 45%, transparent 75%),
      linear-gradient(160deg, #6f8f4a 0%, #c7c2bb 25%, var(--photo-mid) 55%, var(--photo-dark) 100%);
  }
  .shapes {
    position: absolute;
    inset: 0;
  }
  .brand-bar {
    position: absolute;
    left: 0;
    top: 62px;
    width: 520px;
    height: 96px;
    background: rgba(255, 255, 255, 0.82);
    display: flex;
    align-items: center;
    gap: 16px;
    padding-left: 48px;
    box-sizing: border-box;
  }
  .brand-mark {
    width: 26px;
    height: 26px;
    background: var(--brand-blue);
  }
  .brand-name {
    font-weight: 700;
    font-size: 27px;
    letter-spacing: 2px;
    color: var(--brand-blue);
  }
  .intro {
    position: absolute;
    left: 48px;
    top: 708px;
    margin: 0;
    font-size: 33px;
    line-height: 48px;
    font-weight: 400;
    color: var(--ink);
    letter-spacing: 0.5px;
  }
  .intro strong {
    display: block;
    font-weight: 700;
    color: var(--brand-blue);
  }
  .offer {
    position: absolute;
    left: 548px;
    top: 818px;
    margin: 0;
    font-size: 64px;
    line-height: 72px;
    font-weight: 800;
    color: var(--brand-blue);
    text-transform: uppercase;
  }
  .promise {
    position: absolute;
    left: 48px;
    top: 1062px;
    margin: 0;
    font-size: 44px;
    line-height: 60px;
    font-weight: 800;
    font-style: italic;
    color: var(--paper);
  }
</style>
</head>
<body>
  <main class="ad-canvas">
    <div class="hero-photo" role="img" aria-label="Business owner at a desk wearing a smartwatch showing heart rate, holding a phone with blood pressure readings"></div>

    <svg class="shapes" width="1200" height="1200" viewBox="0 0 1200 1200" aria-hidden="true">
      <path class="mist-band" d="M0,528 L800,752 L0,592 Z" fill="var(--mist)"/>
      <path class="content-panel" d="M0,580 L880,772 Q1000,795 1060,700 L1200,470 L1200,1200 L0,1200 Z" fill="var(--paper)"/>
      <path class="accent-line" d="M0,480 L860,726 Q960,752 1015,676 L1200,372" fill="none" stroke="var(--accent-orange)" stroke-width="3"/>
      <path class="rule-line" d="M0,922 L1060,1200" fill="none" stroke="var(--mist)" stroke-width="4"/>
      <path class="promise-band" d="M0,935 L1010,1200 L0,1200 Z" fill="var(--accent-orange)"/>
    </svg>

    <div class="brand-bar">
      <span class="brand-mark"></span>
      <span class="brand-name">BLUEFERN REWARD GROUP</span>
    </div>

    <p class="intro">
      <strong>Boost responses</strong>
      to your ads without<br>
      increasing ad spend<br>
      giving away
    </p>

    <h1 class="offer">Free<br>Smartwatches<br>and Sonettes</h1>

    <p class="promise">Don't Personally<br>Need To Fulfill!</p>
  </main>
</body>
</html>
```